Real Estate Development Sign

I am trying to get some good graphic design help for a new real estate development project. We need two designs for two separate large billboard-type directionals, also For Sale Signs, and also bandit directional signs. I have a company who have already given it a shot, but I don't like what they have come up with. I need it to have a WOW factor and pop to catch people's eye, but also simple and easy to read. I've attached what they have done so far. I have proofs of what has already been created and I've attached them. I've also attached the logo for the project, but I'm fine with changing the color for the logo to help make the overall signs more cohesive. I want clean, easy to read and eye catching. I will need to be able to pass the designs on to a company to have them printed for the billboards. One of them is 10x12 and the other is 8x10. Time is of the essence - I've spent too much time trying to get this other company to do what I want.
Updates

Project Deadline Extended
Reason: Need more submissions.

I would like to shoot for Black, Red, White and a touch of Yellow for the colors of the signs.

Industry/Entity Type

Graphic Design

```html
<!DOCTYPE html>
<html lang="en">
<head>
<meta charset="utf-8">
<title>Marlow Homes – For Sale Sign</title>
<link rel="stylesheet" href="https://fonts.googleapis.com/css2?family=Jost:wght@500;600&display=swap">
<style>
  :root {
    --sign-green: #1b5030;
    --sign-yellow: #ffff00;
    --sign-red: #d40000;
    --sign-black: #1e1e1e;
    --sign-white: #ffffff;
  }
  html, body {
    margin: 0;
    padding: 0;
    width: 900px;
    height: 1200px;
    overflow: hidden;
    background: var(--sign-white);
  }
  .sign {
    display: block;
    width: 900px;
    height: 1200px;
  }
  .sign-text {
    font-family: "Jost", "Century Gothic", sans-serif;
  }
  .band-green { fill: var(--sign-green); }
  .band-black { fill: var(--sign-black); }
  .brand-name { fill: var(--sign-yellow); font-size: 132px; font-weight: 600; }
  .headline { fill: var(--sign-red); font-size: 178px; font-weight: 500; }
  .agent-name { fill: var(--sign-white); font-size: 80px; font-weight: 600; }
  .agent-phone { fill: var(--sign-white); font-size: 106px; font-weight: 500; }
</style>
</head>
<body>
<svg class="sign" viewBox="0 0 900 1200" xmlns="http://www.w3.org/2000/svg">
  <!-- Brand header -->
  <rect class="band-green" x="0" y="0" width="900" height="292"/>
  <polygon class="band-green" points="0,306 900,306 900,406 600,406 552,360 0,360"/>
  <text class="sign-text brand-name" x="78" y="168" textLength="738" lengthAdjust="spacingAndGlyphs">MARLOW HOMES</text>

  <!-- Headline -->
  <text class="sign-text headline" x="54" y="630" textLength="810" lengthAdjust="spacingAndGlyphs">FOR SALE</text>

  <!-- Agent footer -->
  <polygon class="band-black" points="0,690 294,690 348,738 900,738 900,786 0,786"/>
  <rect class="band-black" x="0" y="802" width="900" height="398"/>
  <text class="sign-text agent-name" x="112" y="946" textLength="674" lengthAdjust="spacingAndGlyphs">MARISA HOLLOWAY</text>
  <text class="sign-text agent-phone" x="198" y="1094" textLength="504" lengthAdjust="spacingAndGlyphs">555.014.2387</text>
</svg>
</body>
</html>
```